Brevanta needs a business Card Design

We are looking for a business card Design for our new Managed Service Provider Company, Brevanta. Brevanta encompasses everything IT for the average medium sized business. Our primary services are help desk support, cyber-security (malware and ransomware protection), and Disaster Recovery systems. We would like the design to have a very clean and professional look, with a very minimalist feel.

Target Market(s)

Medium to large sized businesses

Industry/Entity Type

It Service

Contact Information for Business Card

Name GoesHere
name@brevanta-mail.net
O: 555-382-6047
C: 555-000-0000

Font styles to use
Other font styles liked:
• Poppins Font Only Please

Colors

Designer to choose only greyscale colors for use in the design.

Requirements
Must have
• Logo included
Nice to have
• Cutting Edge, innovative, minimalistic, elegant

```html
<!DOCTYPE html>
<html lang="en">
<head>
<meta charset="utf-8">
<title>Brevanta – Business Card</title>
<link rel="stylesheet" href="https://fonts.googleapis.com/css2?family=Poppins:wght@300;400;600&display=swap">
<style>
  :root {
    --stage: #e4e4e4;
    --charcoal: #1e1e1e;
    --paper: #ffffff;
    --ink: #1e1e1e;
    --ink-soft: #4a4a4a;
    --on-dark: #ffffff;
    --on-dark-soft: #d6d6d6;
  }
  * { box-sizing: border-box; margin: 0; padding: 0; }
  html, body { width: 1200px; height: 900px; overflow: hidden; }
  body {
    background: var(--stage);
    font-family: "Poppins", sans-serif;
    position: relative;
  }
  .card {
    position: absolute;
    width: 620px;
    height: 354px;
    border-radius: 26px;
    box-shadow: 0 6px 18px rgba(0,0,0,0.12);
    overflow: hidden;
  }

  /* Back side */
  .card-back {
    left: 160px; top: 70px;
    background: var(--charcoal);
    color: var(--on-dark);
  }
  .card-back .brand-mark {
    position: absolute;
    left: 50%; top: 92px;
    width: 34px; height: 34px;
    margin-left: -17px;
    background: var(--on-dark);
  }
  .card-back .wordmark {
    position: absolute;
    left: 0; right: 0; top: 150px;
    text-align: center;
    font-weight: 300;
    font-size: 30px;
    letter-spacing: 16px;
    padding-left: 16px;
  }
  .card-back .services {
    position: absolute;
    left: 0; right: 0; bottom: 38px;
    text-align: center;
    font-weight: 300;
    font-size: 13px;
    letter-spacing: 0.3px;
    color: var(--on-dark-soft);
  }

  /* Front side */
  .card-front {
    left: 420px; top: 470px;
    background: var(--paper);
    color: var(--ink);
  }
  .card-front .brand-block {
    position: absolute;
    right: 48px; top: 42px;
    width: 190px; height: 190px;
    background: var(--charcoal);
  }
  .card-front .wordmark {
    position: absolute;
    left: 40px; top: 122px;
    font-weight: 300;
    font-size: 30px;
    letter-spacing: 15px;
    color: var(--ink);
  }
  .card-front .person {
    position: absolute;
    left: 40px; top: 200px;
  }
  .person .name {
    font-weight: 600;
    font-size: 18px;
    line-height: 1.1;
    letter-spacing: 0.3px;
  }
  .person .role {
    font-weight: 400;
    font-size: 15px;
    line-height: 1.2;
    color: var(--ink-soft);
  }
  .contact-list {
    position: absolute;
    left: 40px; top: 262px;
    list-style: none;
  }
  .contact-list li {
    display: flex;
    align-items: center;
    gap: 10px;
    font-size: 14px;
    line-height: 22px;
    color: var(--ink-soft);
  }
  .contact-list svg { width: 15px; height: 15px; fill: var(--ink); flex: none; }
</style>
</head>
<body>

  <section class="card card-back">
    <div class="brand-mark"></div>
    <div class="wordmark">BREVANTA</div>
    <p class="services">Help desk support | Cyber-security | Disaster Recovery systems</p>
  </section>

  <section class="card card-front">
    <div class="brand-block"></div>
    <div class="wordmark">BREVANTA</div>
    <div class="person">
      <p class="name">DANIEL HARLOW</p>
      <p class="role">Managing Director</p>
    </div>
    <ul class="contact-list">
      <li>
        <svg viewBox="0 0 16 16" aria-hidden="true"><path d="M1 5c0-2 3-3 7-3s7 1 7 3v1h-3V5H4v1H1z M3 8h10l1 6H2z M8 9.5a2 2 0 1 0 0 4a2 2 0 1 0 0-4z"/></svg>
        555-382-6047
      </li>
      <li>
        <svg viewBox="0 0 16 16" aria-hidden="true"><path d="M4 1h8v14H4z M5.5 3v9h5V3z M7 13h2v1H7z"/></svg>
        555-000-0000
      </li>
      <li>
        <svg viewBox="0 0 16 16" aria-hidden="true"><path d="M1 3h14v10H1z M2.5 4.5 8 9l5.5-4.5v-.2H2.5z"/></svg>
        name@brevanta-mail.net
      </li>
    </ul>
  </section>

</body>
</html>
```